Webiste Design KLV

Design the website using uploaded content. Design colors should match that of the company logo with an allowance of one more extra color if it makes the website look much better and colorful. Use Technology related stock images in your design.

Target Market(s)

Potential Clients - Companies

Industry/Entity Type

Information Technology

Coding

Coded - Design and coding required

Number of Pages Required

5+ page

Requirements
Must have
• Company Logo Colors
Nice to have
• Professional Look and Feel with Sliders showing professional information technology images

```html
<!DOCTYPE html>
<html lang="en">
<head>
<meta charset="utf-8">
<title>KLV Technologies — ICT and Engineering Company</title>
<link href="https://fonts.googleapis.com/css2?family=Mulish:wght@300;400;600;700;800&family=Playfair+Display:wght@700;800&display=swap" rel="stylesheet">
<style>
:root{
  --orange:#f7901e;
  --orange-dark:#e57c0b;
  --blue:#1f4fd0;
  --blue-deep:#1a2f9a;
  --purple:#8781d6;
  --ink:#1d2233;
  --text:#4a4f5e;
  --muted:#8a8f9c;
  --light:#eef0f6;
  --slate:#2d3348;
  --slate-card:#242a3d;
  --navy:#141a2d;
  --night:#0e0f1d;
  --white:#ffffff;
}
*{box-sizing:border-box;margin:0;padding:0}
html,body{width:1200px;height:5021px;overflow:hidden}
body{font-family:'Mulish',Arial,sans-serif;color:var(--text);background:var(--white);position:relative}
.serif{font-family:'Playfair Display',Georgia,serif}
section,header,footer,nav{position:relative;display:block;width:1200px;overflow:hidden}
.abs{position:absolute}
.btn{position:absolute;display:flex;align-items:center;gap:10px;background:var(--orange);color:var(--white);font-size:12px;font-weight:600;letter-spacing:.5px;padding:0 14px;height:40px;text-transform:uppercase}
.btn .dot{width:20px;height:20px;border-radius:50%;background:var(--white);display:flex;align-items:center;justify-content:center}
.eyebrow{font-size:13px;text-transform:uppercase;letter-spacing:.3px}
.placeholder{position:absolute}

/* top bar */
.topbar{height:43px;background:var(--orange)}
.topbar .contact-strip{position:absolute;left:600px;top:0;width:600px;height:43px;background:#2b2b2b;display:flex;justify-content:flex-end;align-items:center;gap:40px;padding-right:105px;color:#ddd;font-size:13px}
.topbar .contact-strip span{display:flex;align-items:center;gap:8px}
.social{display:flex;gap:14px;position:absolute;left:107px;top:11px}
.social i{width:22px;height:22px;border-radius:50%;background:var(--white);display:block}

/* nav */
.nav{height:89px;background:var(--white);box-shadow:0 1px 4px rgba(0,0,0,.06)}
.brand{position:absolute;left:107px;top:27px;display:flex;align-items:center;gap:10px;font-weight:800;font-size:32px;line-height:36px;color:var(--orange);letter-spacing:1px}
.brand .mark{width:22px;height:22px;background:var(--orange)}
.menu{position:absolute;right:107px;top:36px;display:flex;gap:42px;font-size:13px;line-height:18px;color:var(--ink);text-transform:uppercase}
.menu .active{color:var(--orange)}

/* hero */
.hero{height:540px;background:linear-gradient(120deg,#1b3fc2 0%,#2160e0 55%,#1a3aa8 100%)}
.hero .art{left:440px;top:0;width:760px;height:510px;background:radial-gradient(circle at 60% 45%,#35a7f2 0%,#2a6ee0 45%,rgba(31,79,208,0) 75%)}
.hero .lead-small{left:107px;top:137px;font-size:25px;color:var(--white);font-weight:300}
.hero h1{position:absolute;left:107px;top:170px;font-size:50px;line-height:60px;color:var(--white)}
.hero p{position:absolute;left:107px;top:315px;width:370px;font-size:13px;line-height:23px;color:#e3e9ff}
.hero .btn{left:107px;top:390px}

/* about */
.about{height:520px;background:var(--purple)}
.about .art{left:20px;top:70px;width:540px;height:350px;background:radial-gradient(ellipse at 50% 55%,#eceaf8 0%,#b3aee6 45%,rgba(135,129,214,0) 75%)}
.about .eyebrow{position:absolute;left:646px;top:85px;color:var(--white)}
.about h2{position:absolute;left:646px;top:105px;font-size:40px;color:var(--white)}
.about p{position:absolute;left:646px;top:180px;width:450px;font-size:14px;line-height:24.5px;color:#f1f0fb}
.about .btn{left:646px;top:388px}

/* pillars */
.pillars{height:503px}
.pillar{position:absolute;top:123px;width:316px;height:355px;border-radius:0 40px 0 40px;overflow:hidden}
.pillar h3{position:absolute;bottom:36px;width:100%;text-align:center;font-size:20px;color:var(--white)}
.p1{left:107px;background:linear-gradient(160deg,#6c6a6e,#2c2b33)}
.p2{left:442px;background:linear-gradient(160deg,#d9a070,#8c5a36)}
.p3{left:775px;background:linear-gradient(160deg,#3d5a78,#121b2b)}

/* services */
.services{height:662px;background:var(--light)}
.services .eyebrow{position:absolute;top:132px;width:100%;text-align:center;color:var(--ink);font-size:13px}
.services h2{position:absolute;top:150px;width:100%;text-align:center;font-size:42px;color:var(--ink)}
.service-card{position:absolute;top:236px;width:316px;height:356px;background:var(--white);padding:32px 30px;box-shadow:0 6px 20px rgba(30,40,80,.08)}
.service-card .icon{width:82px;height:82px;border-radius:22px;background:var(--orange);display:flex;align-items:center;justify-content:center}
.service-card h3{margin-top:30px;font-size:19px;font-weight:600;color:var(--ink)}
.service-card p{margin-top:18px;font-size:13px;line-height:23px;color:var(--text)}
.service-card a{position:absolute;left:32px;bottom:30px;font-size:12px;font-weight:700;color:var(--orange);text-decoration:underline;text-transform:uppercase}

/* industries */
.industries{height:614px}
.industries .art{left:40px;top:40px;width:535px;height:420px;background:radial-gradient(ellipse at 50% 50%,#dfe6fb 0%,#b9c7f3 40%,rgba(255,255,255,0) 72%)}
.industries .eyebrow{position:absolute;left:616px;top:98px;color:var(--ink)}
.industries h2{position:absolute;left:616px;top:116px;font-size:42px;color:var(--ink)}
.industries p{position:absolute;left:616px;top:197px;width:480px;font-size:14px;line-height:24.5px;color:var(--text)}
.industries .btn{left:616px;top:418px}

/* governance */
.governance{height:604px;background:var(--slate)}
.governance .eyebrow{position:absolute;top:54px;width:100%;text-align:center;color:#dfe2ec}
.governance h2{position:absolute;top:74px;width:100%;text-align:center;font-size:40px;color:var(--white)}
.governance .intro{position:absolute;top:142px;left:200px;width:800px;text-align:center;font-size:13px;line-height:23px;color:#dfe2ec}
.value-card{position:absolute;top:224px;width:316px;height:331px;background:var(--slate-card);border-top:4px solid var(--orange);text-align:center;padding:44px 28px 0}
.value-card.featured{background:var(--white)}
.value-card h3{margin-top:20px;font-size:19px;color:var(--white)}
.value-card.featured h3{color:var(--ink)}
.value-card h3 em{font-style:normal;color:var(--orange)}
.value-card p{margin-top:22px;font-size:13px;line-height:23px;color:#d1d5e0}
.value-card.featured p{color:var(--text)}
.value-card .more{color:var(--orange);font-size:13px}

/* contact */
.contact{height:652px;background:var(--navy)}
.contact .eyebrow{position:absolute;left:107px;top:255px;color:#dfe2ec}
.contact h2{position:absolute;left:107px;top:272px;font-size:40px;color:var(--white)}
.contact .loc-label{position:absolute;left:107px;top:352px;font-size:16px;font-weight:700;color:var(--white)}
.contact .loc{position:absolute;left:107px;top:378px;font-size:12px;color:#c6cad6}
.reach{position:absolute;top:424px;display:flex;gap:14px;align-items:center}
.reach .badge{width:40px;height:40px;border-radius:50%;background:var(--orange);display:flex;align-items:center;justify-content:center}
.reach b{display:block;font-size:16px;color:var(--white)}
.reach span{font-size:12px;color:#c6cad6}
.quote{position:absolute;left:577px;top:165px;width:623px;height:410px;background:var(--light);border-left:8px solid var(--orange)}
.quote h3{position:absolute;left:40px;top:58px;font-size:28px;font-weight:600;color:var(--ink)}
.field{position:absolute;left:40px;width:226px;height:44px;background:var(--white);font-size:11px;color:#666;padding:15px 10px}
.field.message{left:272px;width:236px;height:215px}
.submit{position:absolute;left:40px;top:330px;width:226px;height:44px;background:var(--orange);color:var(--white);font-size:11px;display:flex;align-items:center;justify-content:center}

/* partners */
.partners{height:313px}
.partners h2{position:absolute;top:85px;width:100%;text-align:center;font-size:40px;color:var(--ink)}
.partner-row{position:absolute;left:107px;top:160px;display:flex;gap:10px}
.partner{width:156px;height:70px;border:1px solid #dcdfe6;display:flex;align-items:center;justify-content:center}
.partner i{width:96px;height:26px;border-radius:4px;background:#d4d8e2;display:block}

/* footer */
.footer{height:481px;background:var(--night)}
.footer .brand{top:160px;left:107px}
.footer .social{left:150px;top:226px}
.fcol{position:absolute;top:100px}
.fcol h4{font-family:'Playfair Display',Georgia,serif;font-size:20px;font-weight:700;color:var(--white);padding-bottom:8px;border-bottom:1px solid #3a3c4e;display:inline-block}
.fcol ul{list-style:none;margin-top:20px}
.fcol li{font-size:13px;color:#d3d5de;line-height:31px}
.news-line{width:244px;border-bottom:1px solid #45475a;font-size:11px;color:#9a9caa;padding-bottom:10px;margin-top:26px}
.subscribe{margin-top:24px;width:138px;height:42px;background:var(--orange);color:var(--white);font-size:12px;display:flex;align-items:center;justify-content:center;text-transform:uppercase}
.copyright{position:absolute;top:442px;width:100%;text-align:center;font-size:11px;color:#d3d5de}
.copyright em{font-style:normal;color:var(--orange)}
</style>
</head>
<body>

<header class="topbar">
  <div class="social"><i></i><i></i><i></i></div>
  <div class="contact-strip">
    <span><svg width="16" height="16" viewBox="0 0 24 24" fill="none" stroke="#ddd" stroke-width="2"><path d="M5 3h4l2 5-3 2a11 11 0 0 0 6 6l2-3 5 2v4a2 2 0 0 1-2 2A17 17 0 0 1 3 5a2 2 0 0 1 2-2z"/></svg>010 555 0199</span>
    <span><svg width="18" height="14" viewBox="0 0 24 18" fill="none" stroke="#ddd" stroke-width="2"><rect x="1" y="1" width="22" height="16"/><path d="M1 1l11 9 11-9"/></svg>hello@klvtech.example</span>
  </div>
</header>

<nav class="nav">
  <div class="brand"><span class="mark"></span>KLV</div>
  <div class="menu">
    <span class="active">Home</span><span>About</span><span>Services</span><span>Solution</span><span>Industries</span><span>Partnership</span><span>Contact Us</span>
  </div>
</nav>

<section class="hero">
  <div class="placeholder art" role="img" aria-label="Isometric illustration of a futuristic city with a laptop showing data dashboards and people at work"></div>
  <div class="abs lead-small">ICT AND</div>
  <h1 class="serif">Engineering<br>Company</h1>
  <p>To provide and run ICT as well as Engineering solutions and services that allows our customers to focus...</p>
  <div class="btn">Get Started <span class="dot"><svg width="8" height="10" viewBox="0 0 8 10"><path d="M2 1l4 4-4 4" stroke="#f7901e" stroke-width="2" fill="none"/></svg></span></div>
  <svg class="abs" style="left:0;bottom:0" width="1200" height="70" viewBox="0 0 1200 70" preserveAspectRatio="none">
    <path d="M0 20 C300 70 700 70 1200 0 L1200 70 L0 70 Z" fill="#f7901e"/>
    <path d="M0 32 C300 78 700 78 1200 12 L1200 70 L0 70 Z" fill="#8781d6"/>
  </svg>
</section>

<section class="about">
  <div class="placeholder art" role="img" aria-label="Isometric illustration of large white ICT letters with small figures of people around them"></div>
  <div class="eyebrow">Welcome to</div>
  <h2 class="serif">KLV Technologies</h2>
  <p>KLV Technologies was founded in 2013 as a Private Company. For Most of its initial existence, the company intends to establish close relationships with its various clients, withthe intension of expanding throughout South Africa. KLV Technologies is dedicated to leveraging emerging technologies to provide the highest level of quality products and services, customer service, and security.</p>
  <div class="btn">Read More <span class="dot"><svg width="8" height="10" viewBox="0 0 8 10"><path d="M2 1l4 4-4 4" stroke="#f7901e" stroke-width="2" fill="none"/></svg></span></div>
</section>

<section class="pillars">
  <div class="pillar p1" role="img" aria-label="Photo of a presenter showing a tablet to a team in a meeting room"><h3 class="serif">Mission Statement</h3></div>
  <div class="pillar p2" role="img" aria-label="Photo of a smiling professional holding a tablet"><h3 class="serif">Vission Statement</h3></div>
  <div class="pillar p3" role="img" aria-label="Photo of a hand touching a glowing network of technology icons"><h3 class="serif">Our Value</h3></div>
</section>

<section class="services">
  <div class="eyebrow">Our Solutions and</div>
  <h2 class="serif">Service Offering</h2>

  <div class="service-card" style="left:107px">
    <div class="icon"><svg width="44" height="40" viewBox="0 0 44 40" fill="none" stroke="#fff" stroke-width="2.5"><rect x="3" y="4" width="38" height="12" rx="2"/><rect x="3" y="22" width="38" height="12" rx="2"/><path d="M9 10h10M9 28h10"/></svg></div>
    <h3>Infrastructure Solutions</h3>
    <p>KLV Technologies has a strong team certified and dedicated resources, both office-based as well as site-based at customer locations spread across the country.</p>
    <a>Read More</a>
  </div>
  <div class="service-card" style="left:442px">
    <div class="icon"><svg width="44" height="44" viewBox="0 0 44 44" fill="none" stroke="#fff" stroke-width="2.5"><circle cx="22" cy="22" r="6"/><circle cx="22" cy="6" r="3"/><circle cx="22" cy="38" r="3"/><circle cx="6" cy="22" r="3"/><circle cx="38" cy="22" r="3"/><path d="M22 9v7M22 28v7M9 22h7M28 22h7"/></svg></div>
    <h3>Converged Communication</h3>
    <p>Converged Communication Systems provides best-in-class IP Telephony / Unified Communications solutions, and delivers pro-active support services for businesses of all sizes.</p>
    <a>Read More</a>
  </div>
  <div class="service-card" style="left:775px">
    <div class="icon"><svg width="44" height="40" viewBox="0 0 44 40" fill="none" stroke="#fff" stroke-width="2.5"><rect x="12" y="3" width="20" height="10"/><rect x="4" y="13" width="36" height="16" rx="2"/><rect x="12" y="24" width="20" height="13"/></svg></div>
    <h3>Managed Print Services</h3>
    <p>KLV Technologies partnership with global leaders Lumetra, Korvane, Tessaro, Lyxon and Haldor give our customers complete peace of mind. It also ensures.</p>
    <a>Read More</a>
  </div>
</section>

<section class="industries">
  <div class="placeholder art" role="img" aria-label="Isometric illustration of a city road with cars and a truck, traffic control building and people working on laptops"></div>
  <div class="eyebrow">Industries</div>
  <h2 class="serif">Transportation</h2>
  <p>Our “Adaptive Urban Traffic Control System (UTC)” is a leading UTC system in the world. It can control urban traffic signal intelligently by traffic data collection, data processing and system optimization. It can mitigate urban traffic congestion by UTC coordinated controlling, and help people to reduce energy consumption, and reduce traffic accidents. The system can connect with series traffic controllers and other NTCIP compatible controllers.</p>
  <div class="btn">Read More <span class="dot"><svg width="8" height="10" viewBox="0 0 8 10"><path d="M2 1l4 4-4 4" stroke="#f7901e" stroke-width="2" fill="none"/></svg></span></div>
</section>

<section class="governance">
  <div class="eyebrow">Governance</div>
  <h2 class="serif">Risk and Ethics</h2>
  <p class="intro">KLV Technologies understands investor concerns and issues of governance; ethics and sustainability which are also high on our agenda.</p>

  <div class="value-card" style="left:107px">
    <svg width="60" height="60" viewBox="0 0 60 60" fill="none" stroke="#fff" stroke-width="2"><rect x="14" y="16" width="32" height="36" rx="3"/><path d="M22 16v-6h16v6M21 30l6 6 12-12"/></svg>
    <h3 class="serif">Integrity</h3>
    <p>We believe that all decisions are made with integrity, being honest with self and with others.</p>
  </div>
  <div class="value-card featured" style="left:442px">
    <svg width="60" height="60" viewBox="0 0 60 60" fill="none" stroke="#1d2233" stroke-width="2"><circle cx="30" cy="24" r="9"/><path d="M16 26a14 14 0 0 1 28 0M14 50c2-9 8-13 16-13s14 4 16 13"/><circle cx="30" cy="45" r="3" stroke="#f7901e"/></svg>
    <h3 class="serif">Customer <em>Services</em></h3>
    <p>We believe that customers can and will take notice of and appreciate great, caring service. We base our efforts on this foundation</p>
  </div>
  <div class="value-card" style="left:775px">
    <svg width="60" height="60" viewBox="0 0 60 60" fill="none" stroke="#fff" stroke-width="2"><rect x="8" y="10" width="16" height="16" rx="2"/><rect x="34" y="10" width="18" height="12" rx="2"/><circle cx="40" cy="42" r="9"/><path d="M24 18h10M16 26v14h15" stroke="#f7901e"/></svg>
    <h3 class="serif">Continuous <em>Improvement</em></h3>
    <p>We believe in not accepting the status quo; we believe in the value of ongoing training in any form. We believe in providing opportunity for...<br><span class="more">[+]</span></p>
  </div>
</section>

<section class="contact">
  <svg class="abs" style="left:0;top:0" width="1200" height="110" viewBox="0 0 1200 110" preserveAspectRatio="none">
    <rect width="1200" height="110" fill="#2d3348"/>
    <path d="M0 40 C250 110 520 60 760 50 C950 42 1100 60 1200 40 L1200 110 L0 110 Z" fill="#f7901e"/>
    <path d="M0 70 C250 120 520 90 760 80 C950 72 1100 90 1200 70 L1200 110 L0 110 Z" fill="#141a2d"/>
  </svg>
  <div class="eyebrow">Get a Quote</div>
  <h2 class="serif">Contact Us</h2>
  <div class="loc-label">Location</div>
  <div class="loc">12 Meridian Road Northgate 0700</div>
  <div class="reach" style="left:107px">
    <span class="badge"><svg width="18" height="18" viewBox="0 0 24 24" fill="none" stroke="#fff" stroke-width="2"><path d="M5 3h4l2 5-3 2a11 11 0 0 0 6 6l2-3 5 2v4a2 2 0 0 1-2 2A17 17 0 0 1 3 5a2 2 0 0 1 2-2z"/></svg></span>
    <div><b>Phone</b><span>010 555 0199</span></div>
  </div>
  <div class="reach" style="left:337px">
    <span class="badge"><svg width="18" height="14" viewBox="0 0 24 18" fill="none" stroke="#fff" stroke-width="2"><rect x="1" y="1" width="22" height="16"/><path d="M1 1l11 9 11-9"/></svg></span>
    <div><b>Email</b><span>info@klvtech.example</span></div>
  </div>

  <div class="quote">
    <h3>REQUEST A QUOTE</h3>
    <div class="field" style="top:102px">Name:</div>
    <div class="field" style="top:159px">Email:</div>
    <div class="field" style="top:216px">Phone:</div>
    <div class="field message" style="top:102px">Type Your Message...</div>
    <div class="submit">SUBMIT</div>
  </div>
</section>

<section class="partners">
  <h2 class="serif">Partnership</h2>
  <div class="partner-row">
    <div class="partner"><i></i></div><div class="partner"><i></i></div><div class="partner"><i></i></div>
    <div class="partner"><i></i></div><div class="partner"><i></i></div><div class="partner"><i></i></div>
  </div>
</section>

<footer class="footer">
  <svg class="abs" style="left:0;top:0" width="1200" height="60" viewBox="0 0 1200 60" preserveAspectRatio="none">
    <rect width="1200" height="60" fill="#ffffff"/>
    <path d="M0 20 C300 40 700 40 1200 0 L1200 60 L0 60 Z" fill="#f7901e"/>
    <path d="M0 36 C300 56 700 56 1200 14 L1200 60 L0 60 Z" fill="#0e0f1d"/>
  </svg>
  <div class="brand"><span class="mark"></span>KLV</div>
  <div class="social"><i></i><i></i><i></i></div>

  <div class="fcol" style="left:430px">
    <h4>Quick Links</h4>
    <ul><li>Home</li><li>Services</li><li>Solution</li><li>Industries</li><li>Partnership</li><li>Contact Us</li></ul>
  </div>
  <div class="fcol" style="left:636px">
    <h4>Help Links</h4>
    <ul><li>Terms &amp; Conditions</li><li>Privacy Ploicy</li><li>About Us</li><li>Support</li><li>Cookies Policy</li></ul>
  </div>
  <div class="fcol" style="left:850px">
    <h4>Newsletter</h4>
    <div class="news-line">Name*</div>
    <div class="news-line">Email*</div>
    <div class="subscribe">Subscribe</div>
  </div>
  <div class="copyright">COPYRIGHT © 2023 <em>KLV TECHNOLOGIES</em>. ALL RIGHTS RESERVED.</div>
</footer>

</body>
</html>
```